Clean professional design needed for landscape property business

We need a logo for a new lawncare, landscaping , property maintenance business called Meadow Trim.
Our services include lawn mowing, garden maintenance, clean ups and some property maintenance.
We want a double sided business card that is clean and very professional using the colour scheme from our logo which is provided.
the business card should have impact as we will use these to drop into people's letterboxes as a marketing drop.
Initially we want to see what you come up with so there is a very wide scope here to work with.
Updates

Project Deadline Extended
Reason: we feel our original deadline was too short. we have extended to give more time for quality submissions.

Target Market(s)

High end property owners who don't wish to do there own gardneing or property maintenance

Industry/Entity Type

Business

Contact Information for Business Card

Name
Postion/ Title
Phone number
mobile
web address
physical address

services offered

Font styles to use
Sans Serif

Requirements
Must have
• curved edges preferrred
Nice to have
• We like the idea of the logo being embossed or etched into the card so it looks like it is below the surface of the card
Should not have
• No stock images or characters.

```html
<!DOCTYPE html>
<html lang="en">
<head>
<meta charset="utf-8">
<title>Meadow Trim – Business Card</title>
<link rel="stylesheet" href="https://fonts.googleapis.com/css2?family=Arimo:wght@400;700&family=Oswald:wght@500&display=swap">
<style>
  :root {
    --backdrop: #2b2b2b;
    --card-grey: #58585a;
    --card-white: #ffffff;
    --brand-green: #7dc21e;
    --text-light: #ececec;
    --text-dark: #4a4a4c;
    --etched: #4c4c4e;
  }
  * { margin: 0; padding: 0; box-sizing: border-box; }
  html, body { width: 1200px; height: 900px; overflow: hidden; }
  body {
    background: var(--backdrop);
    font-family: "Arimo", Arial, sans-serif;
    position: relative;
  }
  .card {
    position: absolute;
    left: 320px;
    width: 560px;
    height: 320px;
    border-radius: 22px;
    overflow: hidden;
    box-shadow: 0 10px 30px rgba(0,0,0,.45);
  }
  .card-front { top: 80px; background: var(--card-grey); }
  .card-back { top: 480px; background: var(--card-white); }

  /* Wordmark */
  .wordmark {
    position: absolute;
    display: flex;
    align-items: center;
    gap: 14px;
    font-weight: 700;
    letter-spacing: -1.5px;
    line-height: 1;
  }
  .wordmark-square {
    width: 22px; height: 22px;
    background: var(--brand-green);
  }
  .card-front .wordmark {
    left: 60px; top: 92px;
    font-size: 58px;
    color: var(--etched);
    text-shadow: 0 1px 0 rgba(255,255,255,.15), 0 -1px 0 rgba(0,0,0,.35);
  }
  .card-back .wordmark {
    left: 120px; top: 70px;
    font-size: 56px;
    color: var(--text-dark);
  }

  /* Services */
  .services {
    position: absolute;
    left: 0; bottom: 56px;
    list-style: none;
  }
  .services li {
    display: flex;
    align-items: center;
    gap: 16px;
    color: var(--text-light);
    font-size: 15px;
    letter-spacing: .6px;
    text-transform: uppercase;
    margin-top: 8px;
  }
  .services li::before {
    content: "";
    width: 24px; height: 11px;
    background: var(--brand-green);
  }

  /* Back */
  .contact-band {
    position: absolute;
    left: 0; right: 0; bottom: 0;
    height: 140px;
    background: var(--card-grey);
    border-top: 3px solid var(--brand-green);
    box-shadow: 0 -6px 0 var(--card-white), 0 -8px 0 var(--brand-green);
  }
  .edge-mark {
    position: absolute;
    width: 5px;
    background: var(--brand-green);
  }
  .edge-mark.left { left: 0; bottom: 22px; height: 40px; }
  .edge-mark.right { right: 0; top: 12px; height: 82px; }
  .person {
    position: absolute;
    left: 28px; bottom: 22px;
  }
  .person-name {
    font-family: "Oswald", "Arial Narrow", sans-serif;
    font-weight: 500;
    font-size: 26px;
    color: var(--brand-green);
    letter-spacing: 1px;
    text-transform: uppercase;
    line-height: 1.1;
  }
  .person-title {
    color: var(--text-light);
    font-size: 15px;
  }
  .contact-list {
    position: absolute;
    right: 26px; top: 16px;
    list-style: none;
    text-align: right;
  }
  .contact-list li {
    display: flex;
    justify-content: flex-end;
    align-items: center;
    gap: 10px;
    color: var(--text-light);
    font-size: 14px;
    line-height: 1.55;
  }
  .contact-list svg { width: 12px; height: 12px; }
  .contact-list .address { margin-top: 10px; font-size: 15px; }
</style>
</head>
<body>

<section class="card card-front" aria-label="Business card front">
  <div class="wordmark">Meadow Trim<span class="wordmark-square"></span></div>
  <ul class="services">
    <li>Lawn mowing</li>
    <li>Garden maintenance</li>
    <li>Clean ups &amp; some property maintenance</li>
  </ul>
</section>

<section class="card card-back" aria-label="Business card back">
  <div class="wordmark">Meadow Trim<span class="wordmark-square"></span></div>
  <div class="contact-band">
    <span class="edge-mark left"></span>
    <span class="edge-mark right"></span>
    <div class="person">
      <div class="person-name">Jordan Hale</div>
      <div class="person-title">Chief Executive Officer</div>
    </div>
    <ul class="contact-list">
      <li>555-210-4471
        <svg viewBox="0 0 12 12" aria-hidden="true"><path d="M2 1l2 0 1 3-1.3 1a6 6 0 0 0 3.3 3.3L8 7l3 1v2c0 .6-.4 1-1 1A9 9 0 0 1 1 2c0-.6.4-1 1-1z" fill="#7dc21e"/></svg>
      </li>
      <li>555-318-2096
        <svg viewBox="0 0 12 12" aria-hidden="true"><rect x="3" y="0.5" width="6" height="11" rx="1" fill="none" stroke="#7dc21e" stroke-width="1.2"/><circle cx="6" cy="9.5" r=".7" fill="#7dc21e"/></svg>
      </li>
      <li>www.meadowtrim.com
        <svg viewBox="0 0 12 12" aria-hidden="true"><circle cx="6" cy="6" r="5" fill="none" stroke="#7dc21e" stroke-width="1.1"/><ellipse cx="6" cy="6" rx="2" ry="5" fill="none" stroke="#7dc21e" stroke-width="1"/><line x1="1" y1="6" x2="11" y2="6" stroke="#7dc21e" stroke-width="1"/></svg>
      </li>
      <li class="address">412 Linden Avenue Suite 200, VA 20100</li>
    </ul>
  </div>
</section>

</body>
</html>
```